Design some Business Cards for an Import/Export Company, with this logo.

I would like to get a business card with this logo.

The company name is korvella.

I'd like different fonts and innovative designs.

Also Use generic names an position :D

```html
<!DOCTYPE html>
<html lang="en">
<head>
<meta charset="utf-8">
<title>Korvella Business Card</title>
<link href="https://fonts.googleapis.com/css2?family=Montserrat:wght@300;400;700&display=swap" rel="stylesheet">
<style>
  :root {
    --backdrop: #cfd1d3;
    --card-paper: #f4f4f4;
    --map-tone: #e4e5e6;
    --band-blue: #3a8fc8;
    --band-blue-light: #4a9fd4;
    --band-dark: #3b3d40;
    --text-dark: #3d3f42;
    --text-mid: #6f7276;
    --text-light: #9a9da1;
    --rule: #8a8d91;
  }
  * { margin: 0; padding: 0; box-sizing: border-box; }
  html, body {
    width: 1200px;
    height: 900px;
    overflow: hidden;
    background: var(--backdrop);
    font-family: "Montserrat", Arial, sans-serif;
  }
  .business-card {
    position: absolute;
    left: 75px;
    top: 150px;
    width: 1050px;
    height: 600px;
    background: var(--card-paper);
    overflow: hidden;
    box-shadow: 0 18px 40px rgba(0, 0, 0, 0.25);
  }
  .card-shapes {
    position: absolute;
    inset: 0;
    width: 1050px;
    height: 600px;
  }
  .holder-name {
    position: absolute;
    left: 590px;
    top: 95px;
    font-size: 30px;
    letter-spacing: 1px;
    color: var(--text-mid);
    text-transform: uppercase;
  }
  .holder-name .first { font-weight: 700; }
  .holder-name .last { font-weight: 300; }
  .holder-role {
    position: absolute;
    left: 590px;
    top: 137px;
    font-size: 19px;
    font-weight: 300;
    letter-spacing: 1px;
    color: var(--text-light);
    text-transform: uppercase;
  }
  .contact-block {
    position: absolute;
    left: 70px;
    color: var(--text-dark);
    text-transform: uppercase;
  }
  .contact-block .rule {
    width: 360px;
    height: 1px;
    background: var(--rule);
    margin-bottom: 16px;
  }
  .contact-block .label {
    font-size: 17px;
    font-weight: 400;
    letter-spacing: 1px;
    margin-bottom: 10px;
  }
  .contact-block .line {
    font-size: 17px;
    font-weight: 400;
    letter-spacing: 0.5px;
    line-height: 1.35;
  }
  .contact-phone { top: 175px; }
  .contact-mail { top: 285px; }
</style>
</head>
<body>
  <div class="business-card">
    <svg class="card-shapes" viewBox="0 0 1050 600" xmlns="http://www.w3.org/2000/svg">
      <defs>
        <radialGradient id="mapGlow" cx="50%" cy="50%" r="55%">
          <stop offset="0%" stop-color="var(--map-tone)" stop-opacity="1"/>
          <stop offset="100%" stop-color="var(--map-tone)" stop-opacity="0"/>
        </radialGradient>
        <linearGradient id="bandBlue" x1="0" y1="1" x2="1" y2="0">
          <stop offset="0%" stop-color="var(--band-blue)"/>
          <stop offset="100%" stop-color="var(--band-blue-light)"/>
        </linearGradient>
      </defs>
      <rect class="world-map-area" role="img" aria-label="Faint world map backdrop"
            x="300" y="10" width="720" height="330" rx="165" fill="url(#mapGlow)"/>
      <polygon class="band-dark" points="600,366 1050,160 1050,290" fill="var(--band-dark)"/>
      <polygon class="band-blue" points="0,480 1050,280 1050,600 0,600" fill="url(#bandBlue)"/>
    </svg>

    <div class="holder-name"><span class="first">Karim</span> <span class="last">Selden</span></div>
    <div class="holder-role">Senior Graphic Designer</div>

    <div class="contact-block contact-phone">
      <div class="rule"></div>
      <div class="label">Phone &amp; Fax</div>
      <div class="line">11 (00) 555 214 380</div>
      <div class="line">+1 555 730 412</div>
    </div>

    <div class="contact-block contact-mail">
      <div class="rule"></div>
      <div class="label">Mail &amp; Website</div>
      <div class="line">info@korvella.com</div>
      <div class="line">www.korvella.com</div>
    </div>
  </div>
</body>
</html>
```